Venture Wreckers Book Needs a Cover Design

We need a cover design for Venture Wreckers, Practical Guidance for Faltering Ventures and Doubting Company Founders. We will publish and ebook first (first priority), followed by a hard cover printed book, and then a soft cover book after a few months. The book includes 40 Venture Wreckers and actions owners can implement to counter them and grow. Some examples of killers: self-sabotage, wild optimism, scamming, addictions, burnout, no plan, procrastination, recklessness, haemorrhaging money, etc. We plan to publish the ebook to Pagelume / Tarvelo standards. We want to see designs that convey professionalism, simplicity and creativity.

Target Market(s)

Small and microbusinesses, including start-ups, proprietorships, cottage industries, home-based, single operator, and businesses with or without employees, including corporations and partnerships with fewer than five employees

Industry/Entity Type

Business

Font styles to use
Sans Serif

Colors

Designer to choose colors to be used in the design.

Requirements
Must have
• Uncluttered, professional
• Title: Venture Wreckers
• Subtitle: Practical Guidance for Faltering Ventures and Doubting Company Founders
• Author: Mel Hartigan
Nice to have
• n/a

```html
<!DOCTYPE html>
<html lang="en">
<head>
<meta charset="utf-8">
<title>Venture Wreckers — Mel Hartigan</title>
<link rel="stylesheet" href="https://fonts.googleapis.com/css2?family=Oswald:wght@400;500;600;700&display=swap">
<style>
  :root {
    --cover-black: #000000;
    --photo-top: #1b1b1d;
    --photo-mid: #0c0c0d;
    --title-white: #ffffff;
    --title-red: #e3121b;
    --title-red-deep: #a30c12;
    --subtitle-grey: #8c8c8c;
  }
  html, body {
    margin: 0;
    padding: 0;
    width: 944px;
    height: 1200px;
    overflow: hidden;
    background: var(--cover-black);
  }
  .cover {
    position: relative;
    width: 944px;
    height: 1200px;
    background: var(--cover-black);
    font-family: "Oswald", "Arial Narrow", sans-serif;
    overflow: hidden;
  }
  .cover__photo {
    position: absolute;
    left: 0;
    top: 0;
    width: 944px;
    height: 560px;
    background: linear-gradient(180deg, var(--photo-top) 0%, var(--photo-mid) 60%, var(--cover-black) 100%);
  }
  .cover__title {
    margin: 0;
  }
  .title__lead {
    position: absolute;
    left: 0;
    top: 500px;
    width: 944px;
    text-align: center;
    color: var(--title-white);
    font-weight: 500;
    font-size: 78px;
    line-height: 1;
    letter-spacing: 0.8em;
    text-indent: 0.8em;
  }
  .title__main {
    position: absolute;
    left: 0;
    top: 570px;
    width: 944px;
    text-align: center;
    font-weight: 700;
    font-size: 156px;
    line-height: 1;
    letter-spacing: -1px;
    color: var(--title-red);
    background: linear-gradient(180deg, var(--title-red) 0%, var(--title-red) 55%, var(--title-red-deep) 100%);
    -webkit-background-clip: text;
    background-clip: text;
    -webkit-text-fill-color: transparent;
  }
  .cover__subtitle {
    position: absolute;
    left: 0;
    top: 728px;
    width: 944px;
    margin: 0;
    text-align: center;
    color: var(--subtitle-grey);
    font-weight: 500;
    font-size: 26px;
    line-height: 37px;
    letter-spacing: 0.13em;
    text-transform: uppercase;
  }
  .cover__author {
    position: absolute;
    left: 0;
    top: 1082px;
    width: 944px;
    margin: 0;
    text-align: center;
    color: var(--title-white);
    font-weight: 500;
    font-size: 50px;
    line-height: 1;
    letter-spacing: 0.68em;
    text-indent: 0.68em;
    text-transform: uppercase;
  }
</style>
</head>
<body>
  <main class="cover">
    <div class="cover__photo" role="img" aria-label="Photograph of a businessman's torso in a dark suit with shirt and tie"></div>
    <h1 class="cover__title">
      <span class="title__lead">VENTURE</span>
      <span class="title__main">WRECKERS</span>
    </h1>
    <p class="cover__subtitle">Practical Guidance for Faltering Ventures<br>and Doubting Company Founders</p>
    <p class="cover__author">Mel Hartigan</p>
  </main>
</body>
</html>
```